Business Card Design for Brambly Consulting

I need business cards for a new company I have started called Brambly Consulting. Brambly Consulting is a new business based out of Columbus Ohio. I will be operating in Ohio as well as nationwide. Brambly Consulting is a professional organization designed to fit your organization's specific needs. We are dedicated to the success of organizations. We handle human resource management, leadership coaching and development, executive training, team building, personality inventories and searches, performance evaluations, temp. services, custom solutions and more. Brambly consulting services a variety of industries such as government agencies, educational systems, board of directors, construction services and more, please visit our website for a full list of services (the website will be important).

I leave the design to you. I am a 45 year old male. I was in the education field for 21 years and 11 years as a superintendent. I like the colors red and black. Don't know what works, I will leave that to you as well. I would like to have it be catchy yet masculine. I have been associated with many organizations over the years both public and private, and will be reaching out to the public and private sector.

I do need a logo...so I leave that to you as well. Company name is Brambly Consulting.

Industry/Entity Type

Construction

Contact Information for Business Card

Gordon T. Brambly, President
Brambly Consulting
47 W.Elmcrest Ave. Suite 318
Arcade at Wexbury Court
Columbus, Ohio 43287

Phone : 330-555-0193
email : gbrambly@bramblyadvisors.example
web : www.bramblyadvisors.example
twitter : @bramblyadvisors
facebook : Brambly Consulting

```html
<!DOCTYPE html>
<html lang="en">
<head>
<meta charset="utf-8">
<title>Brambly Consulting – Business Card</title>
<link rel="stylesheet" href="https://fonts.googleapis.com/css2?family=Old+Standard+TT:wght@400;700&display=swap">
<style>
  :root {
    --card-blue: #4094ff;
    --card-white: #ffffff;
    --ink: #141414;
    --page: #e9e9e9;
  }
  * { margin: 0; padding: 0; box-sizing: border-box; }
  html, body {
    width: 1200px;
    height: 686px;
    overflow: hidden;
    background: var(--page);
  }
  .card {
    position: relative;
    width: 1200px;
    height: 686px;
    background: var(--card-blue);
    overflow: hidden;
    font-family: "Old Standard TT", "Century Schoolbook", serif;
    color: var(--ink);
  }
  .card__panel {
    position: absolute;
    inset: 0;
    width: 1200px;
    height: 686px;
  }
  .card__text {
    position: absolute;
    line-height: 1;
    white-space: nowrap;
  }
  .company-name {
    left: 72px;
    top: 261px;
    font-size: 34px;
    font-weight: 700;
    letter-spacing: 0.5px;
  }
  .address-line {
    left: 27px;
    font-size: 31px;
    font-weight: 400;
  }
  .address-line--street { top: 434px; }
  .address-line--building { top: 484px; left: 25px; }
  .address-line--state { top: 534px; left: 30px; font-size: 35px; }

  .person-name {
    left: 763px;
    top: 163px;
    font-size: 36px;
    font-weight: 700;
    letter-spacing: 0.5px;
  }
  .person-title {
    left: 831px;
    top: 218px;
    font-size: 36px;
    font-weight: 400;
  }
  .contact {
    left: 799px;
    font-weight: 400;
  }
  .contact--phone { top: 298px; font-size: 37px; }
  .contact--email { top: 355px; font-size: 23px; }
  .contact--web { top: 406px; font-size: 25px; }

  .icon {
    position: absolute;
    fill: var(--ink);
  }
  .icon--phone { left: 737px; top: 300px; width: 48px; height: 32px; }
  .icon--email { left: 742px; top: 355px; width: 38px; height: 20px; }
  .icon--web { left: 740px; top: 395px; width: 40px; height: 40px; }
</style>
</head>
<body>
  <div class="card">
    <svg class="card__panel" viewBox="0 0 1050 600" preserveAspectRatio="none" aria-hidden="true">
      <path fill="var(--card-white)" d="M0 0 H472 C560 80 592 190 590 290 C588 400 540 510 440 600 H0 Z"/>
    </svg>

    <div class="card__text company-name">Brambly Consulting</div>

    <div class="card__text address-line address-line--street">47 W.Elmcrest Ave. Suite 318</div>
    <div class="card__text address-line address-line--building">Arcade at Wexbury Court Columbus</div>
    <div class="card__text address-line address-line--state">Ohio 43287</div>

    <div class="card__text person-name">Gordon T. Brambly</div>
    <div class="card__text person-title">President</div>

    <svg class="icon icon--phone" viewBox="0 0 48 32" aria-hidden="true">
      <path d="M2 11 C2 4 12 1 24 1 C36 1 46 4 46 11 L46 14 L36 14 L35 9 C30 8 18 8 13 9 L12 14 L2 14 Z"/>
      <path d="M14 13 L34 13 L42 22 L42 31 L6 31 L6 22 Z"/>
      <circle cx="24" cy="22" r="5" fill="var(--card-blue)"/>
    </svg>
    <div class="card__text contact contact--phone">330-555-0193</div>

    <svg class="icon icon--email" viewBox="0 0 38 20" aria-hidden="true">
      <rect x="0" y="0" width="38" height="20"/>
      <path d="M2 2 L19 12 L36 2" fill="none" stroke="var(--card-blue)" stroke-width="1.6"/>
      <path d="M2 18 L14 9 M36 18 L24 9" fill="none" stroke="var(--card-blue)" stroke-width="1.4"/>
    </svg>
    <div class="card__text contact contact--email">gbrambly@bramblyadvisors.example</div>

    <svg class="icon icon--web" viewBox="0 0 40 40" aria-hidden="true">
      <g fill="none" stroke="var(--ink)" stroke-width="2.4">
        <circle cx="20" cy="20" r="18"/>
        <ellipse cx="20" cy="20" rx="8" ry="18"/>
        <line x1="20" y1="2" x2="20" y2="38"/>
        <line x1="2" y1="20" x2="38" y2="20"/>
        <path d="M5 11 H35 M5 29 H35"/>
      </g>
    </svg>
    <div class="card__text contact contact--web">www.bramblyadvisors.example</div>
  </div>
</body>
</html>
```